Pet business needs a business card

Pet shop needs a business card. Like dark background and and debased look.

Hedgerowpups
Lindelaan 27
B - 3270 Korbeek
Belgium

www.hedgerowpups.example
mail@hedgerowpups.example
Phone +32471869203

I will ad a tagline shortly.

Industry/Entity Type

Shop

Font styles to use
Sans Serif

Requirements
Must have
• Must be possible to print the card debased. See example image.

```html
<!DOCTYPE html>
<html lang="en">
<head>
<meta charset="utf-8">
<title>Hedgerowpups business card</title>
<link rel="stylesheet" href="https://fonts.googleapis.com/css2?family=Open+Sans:wght@400;700&display=swap">
<style>
  :root {
    --backdrop: #4a4a4c;
    --card-dark: #2e3038;
    --card-light: #ffffff;
    --accent: #f7962b;
    --text-light: #ffffff;
  }
  html, body {
    margin: 0;
    padding: 0;
    width: 1200px;
    height: 999px;
    overflow: hidden;
    background: var(--backdrop);
    font-family: "Open Sans", Arial, sans-serif;
  }
  .stage { position: relative; width: 1200px; height: 999px; }
  .card { position: absolute; display: block; }
  .card--front { left: 77px; top: 96px; }
  .card--back { left: 348px; top: 535px; }
  .card-base { fill: var(--card-dark); }
  .card-panel { fill: var(--card-light); }
  .accent-line { stroke: var(--accent); stroke-width: 5; fill: none; }
  .brand-name { fill: var(--accent); font-weight: 700; font-family: "Open Sans", Arial, sans-serif; }
  .contact-name { fill: var(--text-light); font-weight: 700; font-size: 19px; }
  .contact-line { fill: var(--text-light); font-weight: 400; font-size: 17px; }
  .icon-tile { fill: var(--accent); }
  .icon-glyph { fill: var(--card-dark); }
  .icon-stroke { fill: none; stroke: var(--accent); stroke-width: 1.5; }
</style>
</head>
<body>
<main class="stage">

  <svg class="card card--front" width="706" height="402" viewBox="0 0 706 402" aria-label="Business card front">
    <rect class="card-base" x="0" y="0" width="706" height="402"/>
    <polygon class="card-panel" points="0,0 453,0 543,277 0,201"/>
    <line class="accent-line" x1="453" y1="0" x2="589" y2="402"/>
    <line class="accent-line" x1="0" y1="201" x2="545" y2="279"/>

    <rect class="icon-tile" x="35" y="125" width="14" height="14"/>
    <text class="brand-name" x="58" y="168" font-size="40">Hedgerowpups</text>

    <text class="contact-name" x="32" y="272" font-family="Open Sans, sans-serif">Hedgerowpups</text>
    <text class="contact-line" x="32" y="296" font-family="Open Sans, sans-serif">Lindelaan 27, B - 3270 Korbeek, Belgium</text>

    <g class="icon icon--phone">
      <rect class="icon-tile" x="31" y="320" width="20" height="20" rx="3"/>
      <path class="icon-glyph" d="M37 324 h3 l1 4 -2 1 q1 3 4 4 l1 -2 4 1 v3 q-1 1 -3 1 q-8 -2 -9 -9 q0 -2 1 -3z"/>
    </g>
    <text class="contact-line" x="65" y="336" font-family="Open Sans, sans-serif">+32471869203</text>

    <g class="icon icon--mail">
      <rect class="icon-tile" x="30" y="355" width="22" height="17" rx="3"/>
      <path d="M32 358 l9 7 9 -7" fill="none" stroke="#2e3038" stroke-width="2"/>
    </g>
    <text class="contact-line" x="65" y="369" font-family="Open Sans, sans-serif">mail@hedgerowpups.example</text>
  </svg>

  <svg class="card card--back" width="706" height="405" viewBox="0 0 706 405" aria-label="Business card back">
    <rect class="card-base" x="0" y="0" width="706" height="405"/>
    <line class="accent-line" x1="517" y1="0" x2="654" y2="405"/>
    <line class="accent-line" x1="0" y1="265" x2="632" y2="353"/>

    <rect class="icon-tile" x="42" y="180" width="22" height="22"/>
    <text class="brand-name" x="80" y="222" font-size="60">Hedgerowpups</text>

    <g class="icon icon--web">
      <circle class="icon-stroke" cx="50" cy="361" r="9"/>
      <ellipse class="icon-stroke" cx="50" cy="361" rx="4" ry="9"/>
      <line class="icon-stroke" x1="41" y1="361" x2="59" y2="361"/>
      <line class="icon-stroke" x1="43" y1="356" x2="57" y2="356"/>
      <line class="icon-stroke" x1="43" y1="366" x2="57" y2="366"/>
    </g>
    <text class="contact-line" x="73" y="367" font-family="Open Sans, sans-serif">www.hedgerowpups.example</text>
  </svg>

</main>
</body>
</html>
```